The Willowmere Clinic Flyer Design

The Willowmere Clinic is a new company providing Dietetic services for people with gastrointestinal disorders. The main client base would be people suffering from Irritable Bowel Syndrome. IBS is a collection of symptoms which (will be individual to the suffer) including constipation/diarrhoea/abdominal pain or discomfort/bloating/belching/flatulence/stomach gurgling/reflux/nausea/urgency/incomplete emptying/fatigue/headaches. IBS affects approx 30% of the population. Previous treatments have generally been ineffectual and include medication, hypnotherapy, healthy eating.
Recently it has been found that the FODMAP diet (a diet low in fermentable Carbohydrates) has been effective in 75% of sufferers.
The Low FODMAP diet is complex and it is highly recommended that it is undertaken only under the supervision of a suitably qualified dietitian. Treatment is available within the QRV but is usually accessible only following consultation with a Gastroenterologist. Most GP's have never heard of this treatment as the research was only published in 2009 in Australia and is yet to filter through to the general practitioner. The Willowmere Clinic is the only clinic in the UK offering dietetic lead specialist services.
I am a member of the ZLO and MVRT (logos provided)
The flyer would be double sided, informing the patient of all the self help steps they could take if they have IBS then recommending that they contact The Willowmere Clinic for specialist advice.
Self Help: Healthy eating, regular meals, good intake of non caffeinated non alcoholic non fizzy drinks, regular exercise, stress management.
The flyer would be left in GP surgeries, Health centres, holistic therapy centres, or through doors.
Target Market(s)
Majority female aged 20-50, able to pay for private services
Industry/Entity Type
Clinic
Look and feel
Each slider illustrates characteristics of the customer's brand and the style your logo design should communicate.

```html
<!DOCTYPE html>
<html lang="en">
<head>
<meta charset="utf-8">
<title>The Willowmere Clinic – IBS Flyer</title>
<link rel="stylesheet" href="https://fonts.googleapis.com/css2?family=Fredoka:wght@700&family=Questrial&family=Oswald:wght@700&family=Federo&family=Arimo&family=Open+Sans:wght@600&display=swap">
<style>
  :root {
    --paper: #ffffff;
    --leaf: #3ddc2a;
    --leaf-dark: #2f8f2a;
    --alert-red: #ee1c24;
    --ibs-blue: #1a1ae0;
    --action-orange: #ff6412;
    --aqua: #3ee0ee;
    --band: #00f2f4;
    --ink: #111111;
    --badge-light: #ffffff;
    --badge-blue: #1f3f9a;
  }
  html, body {
    margin: 0;
    padding: 0;
    overflow: hidden;
    background: var(--paper);
  }
  .flyer {
    position: relative;
    width: 1200px;
    height: 850px;
    background: var(--paper);
    overflow: hidden;
  }
  .symptoms-heading {
    position: absolute;
    left: 108px;
    top: 38px;
    margin: 0;
    font: 700 43px/1 "Fredoka", sans-serif;
    color: var(--leaf);
    letter-spacing: 2.5px;
  }
  .question-mark-art {
    position: absolute;
    left: 354px;
    top: 14px;
    width: 60px;
    height: 86px;
    border-radius: 30px 30px 10px 10px;
    background: radial-gradient(circle at 45% 35%, #7fd44a, #3d9a2a);
  }
  .symptom-list {
    position: absolute;
    left: 56px;
    top: 106px;
    width: 354px;
    margin: 0;
    padding: 0;
    list-style: none;
  }
  .symptom-list li {
    height: 38.3px;
    margin-bottom: 1.4px;
    border-right: 2px solid var(--leaf-dark);
    border-bottom: 2px solid transparent;
    border-image: linear-gradient(to right, rgba(47,143,42,0), var(--leaf-dark)) 1;
    text-align: center;
    font: 21px/36px "Arimo", Arial, sans-serif;
    color: var(--alert-red);
    box-sizing: border-box;
  }
  .stat-line {
    position: absolute;
    left: 430px;
    width: 730px;
    top: 72px;
    margin: 0;
    text-align: center;
    font: 30px/1.2 "Questrial", sans-serif;
    color: var(--alert-red);
    letter-spacing: 0.7px;
  }
  .condition-name {
    position: absolute;
    left: 464px;
    top: 126px;
    margin: 0;
    font: 400 51px/1.2 "Questrial", sans-serif;
    color: var(--ibs-blue);
    letter-spacing: 0.6px;
    white-space: nowrap;
  }
  .call-to-action {
    position: absolute;
    margin: 0;
    font: 700 44px/1 "Oswald", Impact, sans-serif;
    white-space: nowrap;
    transform: scaleX(1.06);
    transform-origin: left;
  }
  .cta-leave { left: 540px; top: 302px; color: var(--action-orange); }
  .cta-old { left: 540px; top: 350px; color: var(--aqua); }
  .cta-new { left: 464px; top: 420px; color: var(--action-orange); }
  .cta-specialist { left: 555px; top: 475px; color: var(--action-orange); }
  .clinic-band {
    position: absolute;
    left: 20px;
    top: 630px;
    width: 1165px;
    height: 200px;
    background: var(--band);
  }
  .clinic-mark {
    position: absolute;
    left: 45px;
    top: 22px;
    width: 136px;
    height: 136px;
    border-radius: 50%;
    border: 3px solid var(--ink);
    box-sizing: border-box;
  }
  .clinic-name {
    position: absolute;
    left: 232px;
    top: 16px;
    margin: 0;
    font: 400 56px/1.05 "Federo", sans-serif;
    color: var(--ink);
  }
  .clinic-name .line-two { display: block; font-size: 66px; }
  .clinic-tagline {
    position: absolute;
    left: 12px;
    bottom: 5px;
    margin: 0;
    font: 600 21px/1 "Open Sans", sans-serif;
    color: var(--paper);
    letter-spacing: 0.4px;
  }
  .membership-label {
    position: absolute;
    left: 898px;
    top: 10px;
    margin: 0;
    font: 600 19px/1 "Open Sans", sans-serif;
    color: var(--ink);
  }
  .badge-professional {
    position: absolute;
    left: 732px;
    top: 40px;
    width: 293px;
    height: 92px;
    background: var(--badge-light);
  }
  .badge-registry {
    position: absolute;
    left: 1033px;
    top: 40px;
    width: 127px;
    height: 126px;
    background: var(--badge-blue);
    border: 2px solid var(--badge-light);
    box-sizing: border-box;
  }
</style>
</head>
<body>
<main class="flyer">
  <h2 class="symptoms-heading">Suffering</h2>
  <div class="question-mark-art" role="img" aria-label="Question mark made of green grass"></div>

  <ul class="symptom-list">
    <li>Reflux</li>
    <li>Fatigue</li>
    <li>Nausea</li>
    <li>Bloating</li>
    <li>Urgency</li>
    <li>Diarrhea</li>
    <li>Belching</li>
    <li>Flatulence</li>
    <li>Headaches</li>
    <li>Constipation</li>
    <li>Stomach gurgling</li>
    <li>Incomplete emptying</li>
    <li>Abdominal pain or discomfort</li>
  </ul>

  <p class="stat-line">30% of the population is affected by</p>
  <h1 class="condition-name">Irritable Bowel Syndrome (IBS)</h1>

  <p class="call-to-action cta-leave">Leave the</p>
  <p class="call-to-action cta-old">old procedure of treatment</p>
  <p class="call-to-action cta-new">Meet the new treatment</p>
  <p class="call-to-action cta-specialist">Meet the specialist</p>

  <footer class="clinic-band">
    <div class="clinic-mark" aria-hidden="true"></div>
    <p class="clinic-name">The Willowmere<span class="line-two">Clinic</span></p>
    <p class="clinic-tagline">The only clinic in the UK offering dietetic lead specialist services</p>
    <p class="membership-label">Member of -</p>
    <div class="badge-professional" role="img" aria-label="ZLO full member badge"></div>
    <div class="badge-registry" role="img" aria-label="MVRT registered badge"></div>
  </footer>
</main>
</body>
</html>
```